Hey There Pinecrest....a heavily based video and picture gallery style website.

Would like a multipage website for videos and pictures. For example, one page/category will be Events. I would like that page to be a thumbnail gallery where the user would click on a thumbnail and the video will play over/hover the the thumbnail page(not go to another page). So when the user closes the player, they are still on the events page. On each page, would like a navigation bar to be able to go to the other pages/categories. And I would like it this way for the other categories as well (people, places, meet the vendors, pictures....) Please view my current website for all pages needed. I only submitted a fraction of images. How should i send the videos? Please contact if questions.
My current website is at www.heytherepinecrest.example

Target Market(s)

male/female, 30-70+ years old

Industry/Entity Type

Entertainment

Coding

Coded - Design and coding required

Number of Pages Required

5+ page

Font styles to use
Sans Serif

Colors
0393ce
00a990
f04a51
f68d4e

Requirements
Must have
• social media links. the video player must play/hover over the current page rather than going to another page. my logo. a calendar page where I can add events to it. a text area under videos for description, photo gallery for each category, the ability to copy a page to use as a template to add more videos and pictures in the future, contact page, the ability to add google ads, affiliate advertising.

```html
<!DOCTYPE html>
<html lang="en">
<head>
<meta charset="utf-8">
<title>Hey There Pinecrest</title>
<link rel="stylesheet" href="https://fonts.googleapis.com/css2?family=Raleway:wght@400;500;600;700&family=Roboto:wght@400;500;700&family=Open+Sans:wght@400;600;700&display=swap">
<style>
:root{
  --brand:#0393ce;
  --ink:#222;
  --muted:#666;
  --white:#fff;
  --dark:#141414;
  --night:#0d0f12;
  --line:#e6e6e6;
  --navy:#233a6b;
}
*{box-sizing:border-box;margin:0;padding:0}
html,body{width:1200px;height:2757px;overflow:hidden;background:var(--white)}
body{position:relative;font-family:"Open Sans",Arial,sans-serif;color:var(--ink)}
.abs{position:absolute}

/* header */
.topbar{position:absolute;left:0;top:0;width:1200px;height:33px;background:var(--brand)}
.topbar .social{position:absolute;right:104px;top:7px;display:flex;gap:14px}
.topbar .social svg{display:block}
.header{position:absolute;left:0;top:33px;width:1200px;height:88px;background:var(--white);border-bottom:1px solid var(--line)}
.brand{position:absolute;left:101px;top:-33px;width:184px;height:121px;background:var(--white);display:flex;align-items:center;justify-content:center;gap:8px}
.brand .dot{width:16px;height:16px;border-radius:50%;background:var(--brand)}
.brand .name{font-family:"Raleway",sans-serif;font-weight:700;font-size:17px;line-height:1.15;color:#1c3b6b}
.nav{position:absolute;top:35px;left:0;width:1200px;font-family:"Raleway",sans-serif;font-size:15px;font-weight:500;color:#333}
.nav a{position:absolute;color:inherit;text-decoration:none;white-space:nowrap;display:flex;align-items:center;gap:3px}
.nav a.active{color:var(--brand)}

/* hero */
.hero{position:absolute;left:0;top:121px;width:1200px;height:504px;
  background:
    radial-gradient(ellipse 520px 200px at 62% 92%,rgba(120,28,24,.55),transparent 70%),
    radial-gradient(ellipse 380px 260px at 18% 55%,rgba(150,96,52,.55),transparent 70%),
    radial-gradient(ellipse 700px 300px at 65% 60%,rgba(70,52,42,.7),transparent 75%),
    linear-gradient(180deg,#0c0a09 0%,#1d1510 45%,#2e1d15 80%,#1a100c 100%)}
.hero h1{position:absolute;top:220px;width:100%;text-align:center;font-family:"Raleway",sans-serif;font-weight:500;font-size:33px;letter-spacing:1px;color:var(--white)}
.hero .play{position:absolute;left:574px;top:284px}

/* section titles */
.section-title{position:absolute;left:0;width:1200px;text-align:center;font-family:"Raleway",sans-serif;font-weight:500;font-size:32px;letter-spacing:1px;color:var(--ink)}
.section-title::after{content:"";display:block;width:64px;height:4px;background:var(--brand);margin:11px auto 0}

/* tiles */
.tile{position:absolute;overflow:hidden;font-family:"Roboto",sans-serif;color:var(--white)}
.tile .shade{position:absolute;inset:0}
.tile .fade{position:absolute;left:0;right:0;bottom:0;height:55%;background:linear-gradient(180deg,transparent,rgba(0,0,0,.72))}

/* recent uploads */
.uploads{position:absolute;left:97px;top:722px;width:1002px;height:375px}
.feature{left:0;top:0;width:546px;height:375px;
  background:
    radial-gradient(ellipse 150px 190px at 80% 22%,rgba(170,120,90,.7),transparent 70%),
    radial-gradient(ellipse 160px 140px at 82% 88%,rgba(90,70,60,.6),transparent 70%),
    linear-gradient(90deg,#050505 0%,#0e0c0b 45%,#2c201a 70%,#1a1210 100%)}
.feature .big{position:absolute;left:57px;top:164px;font-size:64px;font-weight:700;line-height:1;letter-spacing:-1px}
.feature .slash{position:absolute;left:118px;top:170px}
.feature .lead{position:absolute;left:263px;top:212px;width:250px;font-size:13.5px;line-height:23px}
.feature .btn{position:absolute;left:231px;top:284px;width:86px;height:27px;border:1px solid #ccc;font-size:10px;display:flex;align-items:center;justify-content:center}
.feature .dots{position:absolute;left:255px;top:341px;display:flex;gap:7px}
.feature .dots i{width:6px;height:6px;border-radius:50%;background:#ddd;display:block}
.thumb{width:226px;height:185px}
.thumb .cap{position:absolute;left:8px;bottom:10px;right:8px}
.thumb .cap b{display:block;font-size:13px;font-weight:500;line-height:18px}
.thumb .cap small{display:block;font-size:8px;color:#ccc;margin-top:2px}

/* most viewed */
.viewed{position:absolute;left:97px;top:1209px;width:1002px;height:272px}
.vid{top:0;width:332px;height:272px}
.vid .meta{position:absolute;left:11px;bottom:15px;display:flex;align-items:flex-start;gap:14px}
.vid .pill{margin-top:2px;width:46px;height:20px;border:1px solid #fff;border-radius:10px;font-size:9px;display:flex;align-items:center;justify-content:center;gap:4px}
.vid .meta b{display:block;font-size:14px;font-weight:500}
.vid .meta small{display:block;font-size:8.5px;color:#ddd;margin-top:4px}
.people{background:
    radial-gradient(ellipse 70px 130px at 80% 55%,rgba(200,180,160,.55),transparent 70%),
    radial-gradient(ellipse 80px 140px at 40% 50%,rgba(70,60,55,.8),transparent 70%),
    radial-gradient(ellipse 120px 90px at 20% 20%,rgba(150,120,90,.5),transparent 70%),
    linear-gradient(160deg,#4e3f34,#241c17)}
.cross{background:
    radial-gradient(ellipse 60px 110px at 40% 65%,rgba(150,95,60,.8),transparent 70%),
    linear-gradient(90deg,#6f655c 0%,#8a8178 35%,#2a2a2a 60%,#7e756b 75%,#595048 100%)}

/* schedule */
.schedule{position:absolute;left:0;top:1546px;width:1200px;height:513px;
  background:
    radial-gradient(ellipse 600px 120px at 50% 100%,rgba(60,30,30,.6),transparent 70%),
    radial-gradient(ellipse 300px 160px at 75% 45%,rgba(70,62,55,.5),transparent 70%),
    linear-gradient(180deg,#111214 0%,#16161a 60%,#1b1414 100%)}
.schedule .section-title{top:40px;color:var(--white)}
.day-nav{position:absolute;left:158px;top:184px;width:72px}
.day-nav .arrow{height:40px;display:flex;align-items:center;justify-content:center}
.day-nav .rule{width:36px;height:1px;background:#555;margin:0 auto}
.day-nav .day{margin:50px 0;width:72px;height:72px;background:var(--brand);color:var(--white);font-size:11px;display:flex;flex-direction:column;align-items:center;justify-content:center;gap:5px}
.session{position:absolute;left:301px;width:760px;height:110px}
.session .avatar{position:absolute;left:0;top:0;width:96px;height:96px;border-radius:50%;background:#222;border:6px solid #3a3a3a;display:flex;align-items:center;justify-content:center}
.session .avatar i{display:block;width:74px;height:74px;border-radius:50%;background:radial-gradient(circle at 50% 40%,#c9b39c,#6f5a4a 75%);border:3px solid #fff}
.session .time{position:absolute;left:127px;top:6px;font-size:12px;font-weight:600;color:var(--brand)}
.session .who{position:absolute;left:127px;top:28px;font-size:12px;font-weight:700;color:var(--white)}
.session .who span{font-weight:400;font-size:10px;color:#bbb;margin-left:14px}
.session p{position:absolute;left:127px;top:54px;width:600px;font-size:11px;line-height:20px;color:#9a9a9a}

/* testimonial */
.quote-avatar{position:absolute;left:563px;top:2187px;width:74px;height:74px;border-radius:50%;border:3px solid var(--brand);padding:3px}
.quote-avatar i{display:block;width:100%;height:100%;border-radius:50%;background:radial-gradient(circle at 50% 40%,#c9b39c,#6f5a4a 75%)}
.quote{position:absolute;left:255px;top:2277px;width:690px;text-align:center;font-family:"Raleway",sans-serif;font-size:11.5px;line-height:21px;color:#555}
.quote-name{position:absolute;top:2355px;left:0;width:1200px;text-align:center;font-size:13px;font-weight:700;letter-spacing:.5px;color:#333}
.stars{position:absolute;left:557px;top:2380px;display:flex;gap:10px}

/* footer */
.footer{position:absolute;left:0;top:2463px;width:1200px;height:294px;background:var(--dark)}
.footer .brand-mark{position:absolute;top:60px;left:0;width:1200px;display:flex;justify-content:center;align-items:center;gap:10px}
.footer .brand-mark .dot{width:18px;height:18px;border-radius:50%;background:#ddd}
.footer .brand-mark .name{font-family:"Raleway",sans-serif;font-weight:700;font-size:20px;line-height:1.15;color:#ddd}
.footer .social{position:absolute;top:176px;left:0;width:1200px;display:flex;justify-content:center;gap:13px}
.footer .social span{width:27px;height:27px;border-radius:50%;background:var(--white);display:flex;align-items:center;justify-content:center}
.footer .social span.primary{background:var(--navy)}
.footer .copy{position:absolute;top:251px;left:0;width:1200px;text-align:center;font-family:"Raleway",sans-serif;font-size:13px;color:#888}
</style>
</head>
<body>

<div class="topbar">
  <div class="social" aria-label="Social media links">
    <svg width="19" height="19" viewBox="0 0 20 20" aria-label="Share"><g fill="none" stroke="#fff" stroke-width="1.8"><circle cx="15" cy="4.5" r="2.5"/><circle cx="5" cy="10" r="2.5"/><circle cx="15" cy="15.5" r="2.5"/><path d="M7.2 8.8l5.6-3M7.2 11.2l5.6 3"/></g></svg>
    <svg width="19" height="19" viewBox="0 0 20 20" aria-label="Link"><g fill="none" stroke="#fff" stroke-width="1.8" stroke-linecap="round"><path d="M8.5 11.5l3-3"/><path d="M9.5 5.5l1.5-1.5a3.2 3.2 0 014.5 4.5L14 10"/><path d="M10.5 14.5L9 16a3.2 3.2 0 01-4.5-4.5L6 10"/></g></svg>
    <svg width="19" height="19" viewBox="0 0 20 20" aria-label="Website"><g fill="none" stroke="#fff" stroke-width="1.6"><circle cx="10" cy="10" r="8"/><ellipse cx="10" cy="10" rx="3.5" ry="8"/><path d="M2 10h16"/></g></svg>
    <svg width="19" height="19" viewBox="0 0 20 20" aria-label="Email"><g fill="none" stroke="#fff" stroke-width="1.7"><rect x="2" y="4.5" width="16" height="11" rx="1"/><path d="M2.5 5l7.5 6 7.5-6"/></g></svg>
    <svg width="19" height="19" viewBox="0 0 20 20" aria-label="Feed"><g fill="none" stroke="#fff" stroke-width="1.9"><path d="M3 9a8 8 0 018 8"/><path d="M3 3.5A13.5 13.5 0 0116.5 17"/></g><circle cx="4" cy="16" r="1.8" fill="#fff"/></svg>
  </div>
</div>
<header class="header">
  <div class="brand"><span class="dot"></span><span class="name">Hey There<br>Pinecrest</span></div>
  <nav class="nav">
    <a class="active" style="left:592px">Home</a>
    <a style="left:669px">Videos<svg width="8" height="8" viewBox="0 0 8 8"><path d="M1 3l3 3 3-3" fill="none" stroke="#888" stroke-width="1.2"/></svg></a>
    <a style="left:754px">Photo Gallery<svg width="8" height="8" viewBox="0 0 8 8"><path d="M1 3l3 3 3-3" fill="none" stroke="#888" stroke-width="1.2"/></svg></a>
    <a style="left:886px">Calendar</a>
    <a style="left:983px">Contact</a>
    <svg class="abs" style="left:1074px;top:1px" width="16" height="16" viewBox="0 0 16 16" aria-label="Search"><circle cx="6.5" cy="6.5" r="4.5" fill="none" stroke="#777" stroke-width="1.6"/><line x1="10" y1="10" x2="14" y2="14" stroke="#777" stroke-width="1.6"/></svg>
  </nav>
</header>

<section class="hero" role="img" aria-label="Speaker on stage addressing a packed auditorium">
  <h1>Welcome to Hey There Pinecrest</h1>
  <svg class="play" width="58" height="58" viewBox="0 0 58 58"><circle cx="29" cy="29" r="27" fill="none" stroke="#0393ce" stroke-width="2.5"/><path d="M23 18 L40 29 L23 40 Z" fill="none" stroke="#0393ce" stroke-width="2.5" stroke-linejoin="round"/></svg>
</section>

<h2 class="section-title" style="top:652px">Recent Uploads</h2>
<div class="uploads">
  <div class="tile feature">
    <div class="shade" role="img" aria-label="Portrait of a woman with tattoos in low light"></div>
    <svg class="slash" width="62" height="130" viewBox="0 0 62 130"><line x1="60" y1="2" x2="2" y2="128" stroke="#aaa" stroke-width="1.2"/></svg>
    <div class="big">Trailer</div>
    <div class="lead">Experience 100 Years of American<br>Fashion in This 2-Minute Video</div>
    <div class="btn">Watch Video</div>
    <div class="dots"><i></i><i></i><i style="background:#888"></i></div>
  </div>
  <div class="tile thumb" style="left:548px;top:0;background:radial-gradient(ellipse 70px 80px at 55% 45%,rgba(190,140,60,.6),transparent 70%),linear-gradient(160deg,#5a4318,#2b1e0c)">
    <div class="shade" role="img" aria-label="Woman in casual dress on a city street at night"></div><div class="fade"></div>
    <div class="cap"><b>Casual &amp; Dressy Fashion Outfits</b><small>by Elsa Marrow</small></div>
  </div>
  <div class="tile thumb" style="left:776px;top:0;background:radial-gradient(ellipse 90px 70px at 55% 35%,rgba(190,180,170,.55),transparent 70%),linear-gradient(160deg,#5e5853,#221f1c)">
    <div class="shade" role="img" aria-label="Close-up of a chrome motorcycle engine"></div><div class="fade"></div>
    <div class="cap"><b>Blacker than black: Custom Motorcycles</b><small>by Elsa Marrow</small></div>
  </div>
  <div class="tile thumb" style="left:548px;top:189px;background:radial-gradient(ellipse 110px 60px at 50% 30%,rgba(200,70,80,.55),transparent 70%),linear-gradient(160deg,#6a1c28,#22090d)">
    <div class="shade" role="img" aria-label="Crowd dancing at a nightclub"></div><div class="fade"></div>
    <div class="cap"><b>The best nightlife for dancing.</b><small>by Elsa Marrow</small></div>
  </div>
  <div class="tile thumb" style="left:776px;top:189px;background:radial-gradient(ellipse 60px 90px at 75% 40%,rgba(200,150,110,.5),transparent 70%),radial-gradient(ellipse 60px 90px at 30% 45%,rgba(120,80,50,.5),transparent 70%),linear-gradient(160deg,#4a2e1a,#1a0f08)">
    <div class="shade" role="img" aria-label="Man and woman in a warm-lit scene"></div><div class="fade"></div>
    <div class="cap"><b>Love with my best friend</b><small>by Elsa Marrow</small></div>
  </div>
</div>

<h2 class="section-title" style="top:1141px">Most Viewed Videos</h2>
<div class="viewed">
  <div class="tile vid people" style="left:0">
    <div class="shade" role="img" aria-label="Group of people in conversation at an event"></div><div class="fade"></div>
    <div class="meta"><span class="pill">&#9656; Play</span><div><b>Clients Think You Are Too Expensive</b><small>Monday, Feb 26, 2016 by Elsa Marrow, 344 Views</small></div></div>
  </div>
  <div class="tile vid cross" style="left:335px">
    <div class="shade" role="img" aria-label="Wooden cross pendant on a cord beside a book"></div><div class="fade"></div>
    <div class="meta"><span class="pill">&#9656; Play</span><div><b>Faith Hope Love wood signs</b><small>Monday, Feb 30, 2016 by Rudi Penn, 220 Views</small></div></div>
  </div>
  <div class="tile vid people" style="left:670px">
    <div class="shade" role="img" aria-label="Group of people in conversation at an event"></div><div class="fade"></div>
    <div class="meta"><span class="pill">&#9656; Play</span><div><b>Clients Think You Are Too Expensive</b><small>Monday, Feb 26, 2016 by Elsa Marrow, 344 Views</small></div></div>
  </div>
</div>

<section class="schedule" role="img" aria-label="Dimly lit auditorium background">
  <h2 class="section-title">Event Schedule</h2>
  <div class="day-nav">
    <div class="arrow"><svg width="10" height="6" viewBox="0 0 10 6"><path d="M1 5l4-4 4 4" fill="none" stroke="#aaa" stroke-width="1.2"/></svg></div><div class="rule"></div>
    <div class="day"><svg width="14" height="14" viewBox="0 0 14 14"><circle cx="7" cy="7" r="6" fill="none" stroke="#fff" stroke-width="1.3"/><path d="M7 3.5V7l2.3 1.5" fill="none" stroke="#fff" stroke-width="1.3"/></svg>Day 1</div>
    <div class="rule"></div><div class="arrow"><svg width="10" height="6" viewBox="0 0 10 6"><path d="M1 1l4 4 4-4" fill="none" stroke="#aaa" stroke-width="1.2"/></svg></div>
  </div>
  <div class="session" style="top:122px">
    <div class="avatar" role="img" aria-label="Speaker portrait"><i></i></div>
    <div class="time">10AM - 12PM</div>
    <div class="who">CORIN HALVEY<span>UX/ UI Designer</span></div>
    <p>At vero eos et accusamus et iusto odio dignissimos ducimus qui blanditiis praesentium voluptatum deleniti atque corrupti quos dolores et quas molestias excepturi sint occaecati cupiditate non provident.</p>
  </div>
  <div class="session" style="top:249px">
    <div class="avatar" role="img" aria-label="Speaker portrait"><i></i></div>
    <div class="time">09AM - 12PM</div>
    <div class="who">TEODOR VANCE<span>Producer, Brightloom</span></div>
    <p>At vero eos et accusamus et iusto odio dignissimos ducimus qui blanditiis praesentium voluptatum deleniti atque corrupti quos dolores et quas molestias excepturi sint occaecati cupiditate non provident.</p>
  </div>
  <div class="session" style="top:376px">
    <div class="avatar" role="img" aria-label="Speaker portrait"><i></i></div>
    <div class="time">09AM - 12PM</div>
    <div class="who">WREN ASBURY<span>CEO, Larkfield Co.</span></div>
    <p>At vero eos et accusamus et iusto odio dignissimos ducimus qui blanditiis praesentium voluptatum deleniti atque corrupti quos dolores et quas molestias excepturi sint occaecati cupiditate non provident.</p>
  </div>
</section>

<h2 class="section-title" style="top:2117px">What Our Customers Say</h2>
<div class="quote-avatar" role="img" aria-label="Customer portrait"><i></i></div>
<p class="quote">It is a long established fact that a reader will be distracted by the readable content of a page when looking at its layout. The point of using Lorem Ipsum is that it has a more-or-less normal distribution of letters, as opposed to using 'Content here, content here', making it look like readable English.</p>
<div class="quote-name">MARLO TRENT</div>
<div class="stars" aria-label="4 out of 5 stars">
  <svg width="14" height="14" viewBox="0 0 24 24"><path d="M12 2l3 7 7.5.6-5.7 5 1.8 7.4L12 18l-6.6 4 1.8-7.4-5.7-5L9 9z" fill="#0393ce"/></svg>
  <svg width="14" height="14" viewBox="0 0 24 24"><path d="M12 2l3 7 7.5.6-5.7 5 1.8 7.4L12 18l-6.6 4 1.8-7.4-5.7-5L9 9z" fill="#0393ce"/></svg>
  <svg width="14" height="14" viewBox="0 0 24 24"><path d="M12 2l3 7 7.5.6-5.7 5 1.8 7.4L12 18l-6.6 4 1.8-7.4-5.7-5L9 9z" fill="#0393ce"/></svg>
  <svg width="14" height="14" viewBox="0 0 24 24"><path d="M12 2l3 7 7.5.6-5.7 5 1.8 7.4L12 18l-6.6 4 1.8-7.4-5.7-5L9 9z" fill="#0393ce"/></svg>
</div>

<footer class="footer">
  <div class="brand-mark"><span class="dot"></span><span class="name">Hey There<br>Pinecrest</span></div>
  <div class="social" aria-label="Social media links">
    <span class="primary"><svg width="13" height="13" viewBox="0 0 20 20"><g fill="none" stroke="#fff" stroke-width="2"><circle cx="15" cy="4.5" r="2.5"/><circle cx="5" cy="10" r="2.5"/><circle cx="15" cy="15.5" r="2.5"/><path d="M7.2 8.8l5.6-3M7.2 11.2l5.6 3"/></g></svg></span>
    <span><svg width="13" height="13" viewBox="0 0 20 20"><g fill="none" stroke="#141414" stroke-width="2" stroke-linecap="round"><path d="M8.5 11.5l3-3"/><path d="M9.5 5.5l1.5-1.5a3.2 3.2 0 014.5 4.5L14 10"/><path d="M10.5 14.5L9 16a3.2 3.2 0 01-4.5-4.5L6 10"/></g></svg></span>
    <span><svg width="13" height="13" viewBox="0 0 20 20"><g fill="none" stroke="#141414" stroke-width="1.8"><circle cx="10" cy="10" r="8"/><ellipse cx="10" cy="10" rx="3.5" ry="8"/><path d="M2 10h16"/></g></svg></span>
    <span><svg width="13" height="13" viewBox="0 0 20 20"><g fill="none" stroke="#141414" stroke-width="1.9"><rect x="2" y="4.5" width="16" height="11" rx="1"/><path d="M2.5 5l7.5 6 7.5-6"/></g></svg></span>
    <span><svg width="13" height="13" viewBox="0 0 20 20"><g fill="none" stroke="#141414" stroke-width="2"><path d="M3 9a8 8 0 018 8"/><path d="M3 3.5A13.5 13.5 0 0116.5 17"/></g><circle cx="4" cy="16" r="1.8" fill="#141414"/></svg></span>
    <span><svg width="13" height="13" viewBox="0 0 20 20"><g fill="none" stroke="#141414" stroke-width="1.9"><path d="M5 14V9a5 5 0 0110 0v5l1.5 2h-13z"/><path d="M8.5 18h3"/></g></svg></span>
  </div>
  <div class="copy">2017 &copy; heytherepinecrest.&nbsp; All rights reserved</div>
</footer>

</body>
</html>
```